kelvodia.gr wordpress makeover

We need a makeover of our wordpress website kelvodia.gr We are a company that provides astrology services via phone either by billable phone number or by prepaid packages.This is what we sell. Moreover, we share everyday astrology related articles to our blog. It will be a multy page website. Our goal is always to sell our phone prepaid packages or to make the visitor of the website call our billable numbers. Our website should have:
-a home page introducing its content (astrologers, call packages, blog section with categories).
-astrologers page (you can see the existing one to understand)
-Phone packages page (eshop page where you can buy prepaid phone packages. woo commerce maybe)
- Blog page divined by categories.
The website should have places for display banners eg. a sidebar.
I will provide some screen shots of websites we like. You can always visit our existing website www.kelvodia.gr to see it for yourself.

Target Market(s)

people seeking for future telling - astrologer services via phone. People who like to be informed about everyday astrology predictions

Industry/Entity Type

Astrology - tarot services via phone

Coding

Coded - Design and coding required

Number of Pages Required

5+ page

Font styles to use
Decorative
Script

Colors
6B429C
8869AF
B7A5CE
E3DAEB
F3F0F8

Requirements
Must have
• -Home page -Astrologers page -Phone packages page (eshop) -Blog page with categories - Made following the guidelines of zintle so as to be efficient in zintle ads marketing. Mobile friendly.
Nice to have
• Nice call to action buttons to call or buy packages. Sidebar with banner ads of maybe our offers.

```html
<!DOCTYPE html>
<html lang="en">
<head>
<meta charset="utf-8">
<title>kelvodia.gr – Astrology by phone</title>
<link rel="stylesheet" href="https://fonts.googleapis.com/css2?family=Poppins:wght@400;500;600;700&family=PT+Serif:wght@400;700&display=swap">
<style>
:root{
  --violet:#5b14cf;
  --violet-bright:#6d22e6;
  --violet-deep:#4a0fb4;
  --violet-soft:#8869af;
  --lilac:#b7a5ce;
  --ink:#0f0f12;
  --panel:#1b1b1f;
  --field:#1e1e22;
  --white:#ffffff;
  --text-dark:#2a2a2a;
  --muted:#555;
}
*{box-sizing:border-box;margin:0;padding:0}
html,body{width:1200px;height:4093px;overflow:hidden}
body{position:relative;background:var(--ink);color:var(--white);font-family:"Poppins",sans-serif}
.abs{position:absolute}
a{color:inherit;text-decoration:none}

/* header */
.logo{font-family:"Poppins",sans-serif;font-weight:400;color:var(--white);display:flex;align-items:center;gap:8px}
.logo-dot{display:inline-block;border-radius:50%;background:var(--white)}
.site-logo{left:104px;top:32px;font-size:34px}
.site-logo .logo-dot{width:20px;height:20px}
.main-nav{left:480px;top:38px;display:flex;gap:18px;font-family:"PT Serif",serif;font-size:17px}
.call-box{left:955px;top:20px}
.call-box .label{display:flex;align-items:center;gap:12px;font-weight:600;font-size:23px}
.call-box .number{font-weight:700;font-size:33px;margin-top:4px;padding-left:6px}

/* hero */
.hero-bg{left:0;top:0;width:1200px;height:720px}
.hero-title{left:104px;top:218px;font-size:43px;font-weight:700;line-height:60px}
.hero-text{left:104px;top:349px;width:400px;font-family:"PT Serif",serif;font-weight:700;font-size:14px;line-height:23px}
.btn{display:inline-flex;align-items:center;justify-content:center;gap:7px;background:var(--violet);color:var(--white);border:2px solid #9b6cf0;border-radius:20px;font-weight:600;font-size:13px;text-transform:uppercase}
.hero-btn{left:104px;top:416px;width:152px;height:34px}
.thumb{border-radius:50%}
.thumb-active{border:3px solid var(--violet-bright);padding:5px}
.slider-dot{left:1013px;top:605px;width:18px;height:18px;border-radius:50%;background:#4a3c8a;border:2px solid #7e6ed0}

/* zodiac */
.zodiac{left:0;top:780px;width:1200px;height:380px}
.sign{position:absolute;width:166px;text-align:center}
.sign-icon{width:84px;height:84px;margin:0 auto;border-radius:14px;background:var(--violet);border:3px solid #8e5af5;box-shadow:0 0 18px rgba(109,34,230,.6);display:flex;align-items:center;justify-content:center;font-size:44px;line-height:1;font-family:"DejaVu Sans","Segoe UI Symbol",sans-serif}
.sign-name{margin-top:12px;font-size:19px;font-weight:500}

/* astrologers */
.astro-bg{left:0;top:1160px;width:1200px;height:660px}
.section-title{width:1200px;left:0;text-align:center;font-weight:700;font-size:32px;text-transform:uppercase}
.section-title.violet{color:var(--violet-bright)}
.portrait{border-radius:50%}
.astro-card{left:470px;top:1367px;width:260px;height:260px;border-radius:50%;border:4px solid var(--violet-bright);background:radial-gradient(circle,#12122a,#07070f);text-align:center;padding:50px 28px 0}
.astro-card h3{font-size:18px;font-weight:600}
.astro-card p{font-family:"PT Serif",serif;font-size:9.5px;line-height:16px;margin-top:6px}
.astro-phone{display:inline-flex;align-items:center;gap:6px;margin-top:10px;background:var(--violet);padding:1px 12px;border-radius:4px;font-weight:700;font-size:30px}
.astro-phone small{font-size:13px;font-weight:600;font-style:normal}

/* packages */
.packages-sub{left:0;width:1200px;top:1908px;text-align:center;font-family:"PT Serif",serif;font-size:15px}
.package{position:absolute;top:1958px;width:229px;height:277px;border:2px solid var(--violet);border-radius:4px;background:rgba(10,10,14,.7)}
.package-head{height:66px;background:var(--violet);display:flex;align-items:center;justify-content:center;font-weight:600;font-size:19px}
.package ul{list-style:none;margin:28px 0 0 52px}
.package li{font-size:17px;line-height:30px;display:flex;align-items:center;gap:8px}
.package li::before{content:"";width:12px;height:12px;border-radius:50%;background:var(--violet-bright)}
.price{position:absolute;left:70px;top:222px;width:88px;height:34px;border-radius:18px;background:var(--violet);border:2px solid #9b6cf0;display:flex;align-items:center;justify-content:center;font-weight:600;font-size:21px}

/* blog */
.blog-bg{left:0;top:2403px;width:1200px;height:757px;background:radial-gradient(ellipse at 50% 40%,#5712cc,#420ba8)}
.card{position:absolute;background:var(--white);border-radius:10px;overflow:hidden;color:var(--text-dark)}
.card h4{font-size:14.5px;font-weight:600;line-height:22px;text-align:center}
.meta{display:flex;align-items:center;justify-content:center;gap:14px;font-size:12px;color:var(--violet);font-weight:500}
.meta span{display:flex;align-items:center;gap:4px}
.card p{font-size:12px;line-height:19px;text-align:center;color:var(--muted)}
.mini{position:absolute;left:715px;width:380px;height:127px;background:var(--white);border-radius:10px;overflow:hidden;color:var(--text-dark)}
.mini .thumb-img{position:absolute;left:4px;top:4px;width:105px;height:119px;border-radius:8px}
.mini h4{position:absolute;left:127px;top:26px;font-size:16px;font-weight:500;line-height:26px}
.mini .meta{position:absolute;left:127px;top:86px;font-size:10.5px;justify-content:flex-start;gap:12px}

/* contact */
.field{position:absolute;background:var(--field);display:flex;align-items:flex-start;gap:10px;padding:17px 16px;font-size:15px;font-weight:500;color:#ddd}
.field svg{flex:none;margin-top:2px}

/* footer */
.footer-logo{left:0;width:1200px;top:3852px;justify-content:center;font-size:46px}
.footer-logo .logo-dot{width:34px;height:34px}
.socials{left:0;width:1200px;top:3925px;display:flex;justify-content:center;gap:14px}
.socials span{width:28px;height:28px;border-radius:50%;background:var(--violet)}
.footer-nav{left:0;width:1200px;top:3978px;display:flex;justify-content:center;gap:20px;font-family:"PT Serif",serif;font-size:18px}
.copyright{left:0;width:1200px;top:4041px;text-align:center;font-size:13px}
</style>
</head>
<body>

<!-- HERO -->
<svg class="abs hero-bg" viewBox="0 0 1200 720" role="img" aria-label="Tarot card, crystal pendulum and amethyst on a violet astrology chart">
  <defs>
    <radialGradient id="heroGrad" cx="45%" cy="45%" r="70%">
      <stop offset="0" stop-color="#5d3fb0"/>
      <stop offset=".5" stop-color="#3a2479"/>
      <stop offset="1" stop-color="#1a1036"/>
    </radialGradient>
  </defs>
  <path d="M0 0H1200V585Q600 735 0 585Z" fill="url(#heroGrad)"/>
  <path d="M175 642Q600 735 1080 626Q600 712 175 642Z" fill="#6a1fe0"/>
</svg>

<header>
  <a class="abs logo site-logo" href="#">kelvodia <span class="logo-dot"></span></a>
  <nav class="abs main-nav">
    <a href="#">Astrologer</a><a href="#">Call Packages</a><a href="#">Latest Blog</a><a href="#">Contact Us</a>
  </nav>
  <div class="abs call-box">
    <div class="label">
      <svg width="30" height="30" viewBox="0 0 30 30" fill="none" stroke="#fff" stroke-width="2"><circle cx="15" cy="15" r="13"/><path d="M10 8l3 3-2 2c1 2 3 4 5 5l2-2 3 3-2 2c-5 0-11-6-11-11z" fill="#fff" stroke="none"/></svg>
      Call Us
    </div>
    <div class="number">18620</div>
  </div>
</header>

<section class="hero">
  <h1 class="abs hero-title">The Zodiac signs For<br>Today, Friday 18/11</h1>
  <p class="abs hero-text">Zodiac signs for today 18/11 ARIES Extra obligations appear that require settlement and as soon as possible.</p>
  <a class="abs btn hero-btn" href="#">Get Started <svg width="12" height="12" viewBox="0 0 12 12"><circle cx="6" cy="6" r="6" fill="#fff"/><path d="M5 3l3 3-3 3" stroke="#5b14cf" stroke-width="1.6" fill="none"/></svg></a>
  <div class="abs thumb thumb-active" style="left:980px;top:142px;width:118px;height:118px">
    <div class="thumb" role="img" aria-label="Crystal on a violet cloth" style="width:100%;height:100%;background:radial-gradient(circle,#9e8ae8,#3d2a8a)"></div>
  </div>
  <div class="abs thumb" role="img" aria-label="Glowing blue crystal ball" style="left:988px;top:288px;width:100px;height:100px;background:radial-gradient(circle,#6fa8ff,#1b2d8a 60%,#120e45)"></div>
  <div class="abs thumb" role="img" aria-label="Golden lit crystal ball" style="left:990px;top:436px;width:98px;height:98px;background:radial-gradient(circle,#ffd27a,#b45a1a 55%,#3b1f2c)"></div>
  <span class="abs slider-dot"></span>
</section>

<!-- ZODIAC -->
<section class="abs zodiac">
  <div class="sign" style="left:104px;top:14px"><div class="sign-icon">♈&#xFE0E;</div><div class="sign-name">Aries</div></div>
  <div class="sign" style="left:270px;top:14px"><div class="sign-icon">♉&#xFE0E;</div><div class="sign-name">Taurus</div></div>
  <div class="sign" style="left:437px;top:14px"><div class="sign-icon">♊&#xFE0E;</div><div class="sign-name">Gemini</div></div>
  <div class="sign" style="left:603px;top:14px"><div class="sign-icon">♋&#xFE0E;</div><div class="sign-name">Cancer</div></div>
  <div class="sign" style="left:767px;top:14px"><div class="sign-icon">♌&#xFE0E;</div><div class="sign-name">Leo</div></div>
  <div class="sign" style="left:934px;top:14px"><div class="sign-icon">♍&#xFE0E;</div><div class="sign-name">Virgin</div></div>
  <div class="sign" style="left:104px;top:174px"><div class="sign-icon">♎&#xFE0E;</div><div class="sign-name">Libra</div></div>
  <div class="sign" style="left:270px;top:174px"><div class="sign-icon">♏&#xFE0E;</div><div class="sign-name">Scorpio</div></div>
  <div class="sign" style="left:437px;top:174px"><div class="sign-icon">♐&#xFE0E;</div><div class="sign-name">Capricorn</div></div>
  <div class="sign" style="left:603px;top:174px"><div class="sign-icon">♑&#xFE0E;</div><div class="sign-name">Aquarius</div></div>
  <div class="sign" style="left:767px;top:174px"><div class="sign-icon">♓&#xFE0E;</div><div class="sign-name">Pisces</div></div>
  <div class="sign" style="left:934px;top:174px"><div class="sign-icon">♒&#xFE0E;</div><div class="sign-name">Pisces</div></div>
</section>

<!-- ASTROLOGERS -->
<div class="abs astro-bg" role="img" aria-label="Person with raised arms at sunset over a terrace" style="background:linear-gradient(180deg,#2a2420 0%,#3a2a22 25%,#1a1716 60%,#111 100%)"></div>
<section class="astrologers">
  <h2 class="abs section-title" style="top:1268px">Astrologers</h2>
  <div class="abs portrait" role="img" aria-label="Portrait of an astrologer with red hair" style="left:105px;top:1370px;width:254px;height:254px;background:radial-gradient(circle at 50% 45%,#c98a6e,#8a3a2a 55%,#2a1a1a)"></div>
  <div class="abs astro-card">
    <h3>Mira Dolanis</h3>
    <p>Powerful psychic. I will help you solve your love and business problems with sure answers through the science of astrology. I am the astrologer you are looking for! A telephone forecast will convince you.</p>
    <div class="astro-phone">18620 <small>24</small></div>
  </div>
  <div class="abs portrait" role="img" aria-label="Portrait of an astrologer with blonde hair and glasses" style="left:841px;top:1370px;width:254px;height:254px;background:radial-gradient(circle at 50% 45%,#e8d6c4,#b59a86 55%,#3c6470)"></div>
  <a class="abs btn" href="#" style="left:527px;top:1673px;width:146px;height:36px">Learn More <svg width="12" height="12" viewBox="0 0 12 12"><circle cx="6" cy="6" r="6" fill="#fff"/><path d="M5 3l3 3-3 3" stroke="#5b14cf" stroke-width="1.6" fill="none"/></svg></a>
</section>

<!-- PACKAGES -->
<section class="packages">
  <h2 class="abs section-title violet" style="top:1852px">Call Packages</h2>
  <p class="abs packages-sub">You choose which speech package you want from the following</p>
  <div class="package" style="left:103px"><div class="package-head">30 Min</div><ul><li>Lorem ipsum</li><li>Lorem ipsum</li><li>Lorem ipsum</li><li>Lorem ipsum</li></ul><div class="price">€ 30</div></div>
  <div class="package" style="left:358px"><div class="package-head">60 Min</div><ul><li>Lorem ipsum</li><li>Lorem ipsum</li><li>Lorem ipsum</li><li>Lorem ipsum</li></ul><div class="price">€ 50</div></div>
  <div class="package" style="left:613px"><div class="package-head">120 Min</div><ul><li>Lorem ipsum</li><li>Lorem ipsum</li><li>Lorem ipsum</li><li>Lorem ipsum</li></ul><div class="price">€ 75</div></div>
  <div class="package" style="left:867px"><div class="package-head">150 Min</div><ul><li>Lorem ipsum</li><li>Lorem ipsum</li><li>Lorem ipsum</li><li>Lorem ipsum</li></ul><div class="price">€ 95</div></div>
  <a class="abs btn" href="#" style="left:527px;top:2282px;width:146px;height:36px">Learn More <svg width="12" height="12" viewBox="0 0 12 12"><circle cx="6" cy="6" r="6" fill="#fff"/><path d="M5 3l3 3-3 3" stroke="#5b14cf" stroke-width="1.6" fill="none"/></svg></a>
</section>

<!-- BLOG -->
<div class="abs blog-bg"></div>
<section class="blog">
  <h2 class="abs section-title" style="top:2512px">Latest Blog</h2>

  <article class="card" style="left:103px;top:2601px;width:285px;height:405px">
    <div role="img" aria-label="Hand laying tarot cards on a wooden table" style="height:190px;background:linear-gradient(160deg,#d9cfc4,#8a6a4a 60%,#3a2a1e)"></div>
    <h4 style="margin:20px 20px 0">The zodiac signs for today, Saturday 11/19</h4>
    <div class="meta" style="margin-top:12px">
      <span><svg width="11" height="11" viewBox="0 0 11 11" fill="none" stroke="#5b14cf" stroke-width="1.3"><rect x="1" y="2" width="9" height="8" rx="1"/><path d="M1 4.5h9M3.5 1v2M7.5 1v2"/></svg>Nov 18, 2022</span>
      <span><svg width="11" height="11" viewBox="0 0 11 11" fill="none" stroke="#5b14cf" stroke-width="1.3"><circle cx="5.5" cy="3.5" r="2.5"/><path d="M1 10.5c0-2.5 2-4 4.5-4s4.5 1.5 4.5 4"/></svg>Kelvodia</span>
    </div>
    <p style="margin:10px 20px 0">Lorem ipsum dolor sit amet, consectetur adipiscing elit, sed do eiusmod tempor incididunt ut labore et dolore magna aliqua.</p>
  </article>

  <article class="card" style="left:410px;top:2601px;width:284px;height:405px">
    <h4 style="margin:24px 22px 0">The zodiac signs for today, Thursday 17/11</h4>
    <div class="meta" style="margin-top:12px">
      <span><svg width="11" height="11" viewBox="0 0 11 11" fill="none" stroke="#5b14cf" stroke-width="1.3"><rect x="1" y="2" width="9" height="8" rx="1"/><path d="M1 4.5h9M3.5 1v2M7.5 1v2"/></svg>Nov 18, 2022</span>
      <span><svg width="11" height="11" viewBox="0 0 11 11" fill="none" stroke="#5b14cf" stroke-width="1.3"><circle cx="5.5" cy="3.5" r="2.5"/><path d="M1 10.5c0-2.5 2-4 4.5-4s4.5 1.5 4.5 4"/></svg>Kelvodia</span>
    </div>
    <p style="margin:10px 20px 0">Lorem ipsum dolor sit amet, consectetur adipiscing elit, sed do eiusmod tempor incididunt ut labore et dolore magna aliqua.</p>
    <div role="img" aria-label="White cloud above a ladder on a blue wall" style="position:absolute;left:0;bottom:0;width:100%;height:192px;background:radial-gradient(ellipse at 50% 25%,#e8eefc 0 18%,#3b5cc8 40%,#1e2f86)"></div>
  </article>

  <article class="mini" style="top:2603px">
    <div class="thumb-img" role="img" aria-label="Illustrated tarot card" style="background:linear-gradient(150deg,#8fd0d8,#e7c97a 50%,#5c7ab8)"></div>
    <h4>Tarot for today,<br>Thursday 11/17</h4>
    <div class="meta"><span><svg width="10" height="10" viewBox="0 0 11 11" fill="none" stroke="#5b14cf" stroke-width="1.3"><rect x="1" y="2" width="9" height="8" rx="1"/><path d="M1 4.5h9"/></svg>Nov 18, 2022</span><span><svg width="10" height="10" viewBox="0 0 11 11" fill="none" stroke="#5b14cf" stroke-width="1.3"><circle cx="5.5" cy="3.5" r="2.5"/><path d="M1 10.5c0-2.5 2-4 4.5-4s4.5 1.5 4.5 4"/></svg>Kelvodia</span></div>
  </article>
  <article class="mini" style="top:2743px">
    <div class="thumb-img" role="img" aria-label="Illustrated tarot card with red drapery" style="background:linear-gradient(150deg,#d8c79a,#c0352e 55%,#6c9ab8)"></div>
    <h4>Tarot for today,<br>Wednesday 11/16</h4>
    <div class="meta"><span><svg width="10" height="10" viewBox="0 0 11 11" fill="none" stroke="#5b14cf" stroke-width="1.3"><rect x="1" y="2" width="9" height="8" rx="1"/><path d="M1 4.5h9"/></svg>Nov 18, 2022</span><span><svg width="10" height="10" viewBox="0 0 11 11" fill="none" stroke="#5b14cf" stroke-width="1.3"><circle cx="5.5" cy="3.5" r="2.5"/><path d="M1 10.5c0-2.5 2-4 4.5-4s4.5 1.5 4.5 4"/></svg>Kelvodia</span></div>
  </article>
  <article class="mini" style="top:2883px">
    <div class="thumb-img" role="img" aria-label="Hands holding a tarot card by candlelight" style="background:radial-gradient(circle at 40% 50%,#b8864a,#3a2418 60%,#140d0a)"></div>
    <h4>Tarot for today,<br>Friday 11/18</h4>
    <div class="meta"><span><svg width="10" height="10" viewBox="0 0 11 11" fill="none" stroke="#5b14cf" stroke-width="1.3"><rect x="1" y="2" width="9" height="8" rx="1"/><path d="M1 4.5h9"/></svg>Nov 18, 2022</span><span><svg width="10" height="10" viewBox="0 0 11 11" fill="none" stroke="#5b14cf" stroke-width="1.3"><circle cx="5.5" cy="3.5" r="2.5"/><path d="M1 10.5c0-2.5 2-4 4.5-4s4.5 1.5 4.5 4"/></svg>Kelvodia</span></div>
  </article>
</section>

<!-- CONTACT -->
<section class="contact">
  <h2 class="abs section-title violet" style="top:3252px;left:-40px">Contact Us</h2>
  <div class="field" style="left:143px;top:3337px;width:288px;height:51px"><svg width="13" height="14" viewBox="0 0 13 14" fill="#ddd"><circle cx="6.5" cy="4" r="3.5"/><path d="M0 14c0-4 3-6 6.5-6s6.5 2 6.5 6z"/></svg>Name</div>
  <div class="field" style="left:456px;top:3337px;width:288px;height:51px"><svg width="14" height="12" viewBox="0 0 14 12" fill="#ddd"><rect y="1" width="14" height="10" rx="1"/><path d="M0 2l7 5 7-5" stroke="#1e1e22" stroke-width="1.4" fill="none"/></svg>Email</div>
  <div class="field" style="left:767px;top:3337px;width:287px;height:51px"><svg width="13" height="13" viewBox="0 0 13 13" fill="#ddd"><path d="M2 0l3 3-2 2c1 2 3 4 5 5l2-2 3 3-2 2C5 13 0 8 0 2z"/></svg>Phone</div>
  <div class="field" style="left:143px;top:3408px;width:911px;height:72px"><svg width="14" height="13" viewBox="0 0 14 13" fill="#ddd"><path d="M1 0h12a1 1 0 011 1v8a1 1 0 01-1 1H6l-4 3v-3H1a1 1 0 01-1-1V1a1 1 0 011-1z"/></svg>Subject</div>
  <div class="field" style="left:143px;top:3497px;width:911px;height:126px"><svg width="14" height="12" viewBox="0 0 14 12" fill="#ddd"><rect y="1" width="14" height="10" rx="1"/><path d="M0 2l7 5 7-5" stroke="#1e1e22" stroke-width="1.4" fill="none"/></svg>Message</div>
  <a class="abs btn" href="#" style="left:522px;top:3665px;width:122px;height:36px">Submit <svg width="12" height="12" viewBox="0 0 12 12"><circle cx="6" cy="6" r="6" fill="#fff"/><path d="M5 3l3 3-3 3" stroke="#5b14cf" stroke-width="1.6" fill="none"/></svg></a>
</section>

<!-- FOOTER -->
<footer>
  <svg class="abs" style="left:0;top:3755px" width="1200" height="338" viewBox="0 0 1200 338">
    <path d="M165 58Q600 -20 1090 58Q600 0 165 58Z" fill="#6a1fe0"/>
    <path d="M0 70Q600 0 1200 70V338H0Z" fill="#000"/>
  </svg>
  <div class="abs logo footer-logo">kelvodia <span class="logo-dot"></span></div>
  <div class="abs socials" aria-label="Social links"><span></span><span></span><span></span><span></span></div>
  <nav class="abs footer-nav"><a href="#">Astrologer</a><a href="#">Call Packages</a><a href="#">Latest Blog</a><a href="#">Contact Us</a></nav>
  <p class="abs copyright">Copyrights © 2022 kelvodia &nbsp;| All Rights Reserved.</p>
</footer>

</body>
</html>
```